Personalized Technology Company Needs a Business Card

I need a double-sided business card. Both sides will have the logo, and the contact information. One side will be black, with the white / gray logo, and the other will be white, with the black / gray logo. The black side will have the text "Custom Gaming PC's" and will have a water-cooled gaming PC image. The white side will have the text "Custom Business Computers & Consulting", and will have a business / enterprise PC image. Feel free to add a conservative image in the background, while the color remains unchanged. I'm uploading the base logo (transparent), so you can modify the colors, both the finished colored logos and an idea of ​​the business card (with the current information, just missing the website, which is www.velmorisystems.com, please add it.) Thank you so much for your effort, I'll be specting your cool designs. Good Luck!

Target Market(s)

Gamers & Entrepreneurs / Business Owners / Chief Technology Officers

Industry/Entity Type

Technology Equipment

Contact Information for Business Card

I need a double-sided business card. Both sides will have the logo, and the contact information. One side will be black, with the white/gray logo, and the other one will be white, with the black/gray logo. The black side will have the text "Custom Gaming PC's" and will have a water-cooled gaming PC image. The white side will have the text "Custom Business Computers & Consulting", and will have a business/enterprise PC image. Feel free to add a conservative image in the background, whilst the color remains unchanged.

I'm uploading the base logo (transparent), so you can modify the colors, both the finished colored logos and an idea of the business card (with the actual information, just missing the website, which is www.velmorisystems.com, please add it.)

Thank you so much for your effort, I'll be specting your cool designs. Good Luck!

Font styles to use
Serif

Colors
000000
757575
ffffff

Requirements
Must have
• Please See Description
Nice to have
• Please See Description
Should not have
• Please See Description

```html
<!DOCTYPE html>
<html lang="en">
<head>
<meta charset="utf-8">
<title>Velmori Systems — Business Card</title>
<link href="https://fonts.googleapis.com/css2?family=Tinos:wght@400;700&display=swap" rel="stylesheet">
<style>
  :root {
    --ink: #000000;
    --gray: #757575;
    --paper: #ffffff;
    --stage: #2b2b2e;
    --taupe: #b3a89d;
    --soft-gray: #d8d8d8;
  }
  * { box-sizing: border-box; margin: 0; padding: 0; }
  html, body { width: 1200px; height: 800px; overflow: hidden; }
  body {
    background: var(--stage);
    font-family: "Tinos", "Times New Roman", serif;
    position: relative;
  }
  .card {
    position: absolute;
    width: 606px;
    height: 346px;
    overflow: hidden;
  }

  /* ---------- Front (black) ---------- */
  .card--dark { left: 80px; top: 40px; background: var(--ink); color: var(--paper); }
  .brand {
    position: absolute;
    display: flex;
    align-items: center;
    gap: 12px;
    font-weight: 700;
    letter-spacing: 3px;
    text-transform: uppercase;
  }
  .brand__mark { width: 22px; height: 22px; background: currentColor; }
  .brand__name { font-size: 30px; line-height: 1; }
  .brand__sub { display: block; font-size: 13px; letter-spacing: 7px; margin-top: 6px; }
  .card--dark .brand { left: 42px; top: 62px; color: var(--soft-gray); }

  .person { position: absolute; left: 42px; top: 150px; }
  .person__name { font-size: 20px; font-weight: 700; }
  .person__role { font-size: 15px; margin-top: 2px; }

  .contact { position: absolute; left: 42px; width: 270px; font-size: 14px; }
  .contact--phones { top: 214px; border-top: 1.5px dotted var(--paper); padding-top: 8px; }
  .contact--web { top: 272px; border-top: 1.5px dotted var(--paper); padding-top: 8px; }
  .contact__row { display: flex; align-items: center; gap: 10px; line-height: 20px; }
  .contact__icon { width: 14px; height: 14px; flex: none; }

  .visual {
    position: absolute;
  }
  .visual--gaming {
    right: 26px; top: 22px; width: 260px; height: 210px;
    background: linear-gradient(135deg, #1c2a3a 0%, #3d5a78 45%, #2a2a2a 70%, #111 100%);
  }
  .tagline {
    position: absolute;
    text-transform: uppercase;
    letter-spacing: 1.5px;
    text-align: center;
  }
  .card--dark .tagline {
    right: 30px; top: 256px; width: 252px; padding: 10px 0;
    border: 2px solid var(--gray); border-radius: 6px;
    font-size: 15px; color: var(--paper);
  }

  /* ---------- Back (white) ---------- */
  .card--light { left: 514px; top: 414px; background: var(--paper); color: var(--ink); }
  .card--light .brand { left: 48px; top: 110px; color: var(--ink); }
  .card--light .brand__sub { color: var(--gray); }
  .visual--business {
    right: 30px; top: 24px; width: 240px; height: 170px;
    background: linear-gradient(160deg, #4a4a4a 0%, #e9eef3 40%, #cfd8e0 70%, #6a6a6a 100%);
  }
  .card--light .tagline {
    right: 30px; bottom: 26px; width: 330px; padding: 14px 0;
    border: 4px solid var(--taupe);
    font-size: 14px; color: var(--ink);
  }
  .social { position: absolute; left: 48px; bottom: 70px; display: flex; gap: 8px; }
  .social__dot { width: 18px; height: 18px; border-radius: 50%; background: var(--ink); }
  .website { position: absolute; left: 48px; bottom: 44px; font-size: 14px; }
</style>
</head>
<body>

<section class="card card--dark" aria-label="Business card, front">
  <div class="brand">
    <span class="brand__mark"></span>
    <span class="brand__name">Velmori<span class="brand__sub">Systems</span></span>
  </div>

  <div class="person">
    <p class="person__name">Marco Ruiz Delan</p>
    <p class="person__role">(CEO &amp; Co-Founder)</p>
  </div>

  <div class="contact contact--phones">
    <p class="contact__row">
      <svg class="contact__icon" viewBox="0 0 14 14"><path d="M3 1h2l1 3-1.5 1a7 7 0 0 0 4.5 4.5L10 8l3 1v2a2 2 0 0 1-2 2A10 10 0 0 1 1 3a2 2 0 0 1 2-2z" fill="#fff"/></svg>
      +52 5814 - 3902
    </p>
    <p class="contact__row">
      <svg class="contact__icon" viewBox="0 0 14 14"><rect x="3" y="1" width="8" height="12" rx="1.5" fill="none" stroke="#fff" stroke-width="1.5"/><circle cx="7" cy="11" r="0.9" fill="#fff"/></svg>
      +52 55 - 4618 - 7351
    </p>
  </div>

  <div class="contact contact--web">
    <p class="contact__row">
      <svg class="contact__icon" viewBox="0 0 14 14"><rect x="1" y="3" width="12" height="8" fill="none" stroke="#fff" stroke-width="1.3"/><path d="M1 3l6 5 6-5" fill="none" stroke="#fff" stroke-width="1.3"/></svg>
      contact@velmorisystems.com
    </p>
    <p class="contact__row">
      <svg class="contact__icon" viewBox="0 0 14 14"><circle cx="7" cy="7" r="6" fill="none" stroke="#fff" stroke-width="1.3"/><ellipse cx="7" cy="7" rx="2.5" ry="6" fill="none" stroke="#fff" stroke-width="1"/><path d="M1 7h12" stroke="#fff" stroke-width="1"/></svg>
      www.velmorisystems.com
    </p>
  </div>

  <div class="visual visual--gaming" role="img" aria-label="Water-cooled gaming PC tower beside a monitor showing a game soldier"></div>
  <p class="tagline">Custom Gaming PC's</p>
</section>

<section class="card card--light" aria-label="Business card, back">
  <div class="visual visual--business" role="img" aria-label="Business desktop, laptop, tablet and phone showing office software"></div>

  <div class="brand">
    <span class="brand__mark"></span>
    <span class="brand__name">Velmori<span class="brand__sub">Systems</span></span>
  </div>

  <div class="social" aria-label="Social media">
    <span class="social__dot"></span>
    <span class="social__dot"></span>
    <span class="social__dot"></span>
  </div>
  <p class="website">www.velmorisystems.com</p>

  <p class="tagline">Custom Business Computers &amp; Consulting</p>
</section>

</body>
</html>
```